Cloud Software Services Business Needs New Website Design

Our client is looking for a really modern design for their cloud services company. We have a logo, but apart from that, if you read the brief fully and digest the wireframes, we hope you will come up with a really amazing end product.

The design of the website should be professional and trustworthy, it is there to inspire confidence in the services and softwares, as well as emphasising the track record of TWN and relative knowledge and competencies.

Given all the cloud-related communications in the messaging on the site, we will need this in either the imagery or icons in the site so that we can connect the messaging with the service offering.

The brand, being black, gives full range for the designer to present a palette that serves the brand, not forgetting the audience are generally IT decision-makers.

Target Market(s)

Managers and Directors Responsible for IT/Cloud Infrastructure

Industry/Entity Type

IT Technology

Number of Pages Required

5+ page

Font styles to use
Sans Serif

Requirements
Must have
• Initial designs which match the brief and wireframes, focus on the homepage and the winning designer will need to supply the internal pages for the website.
Nice to have
• Clearly considered professional website designs, with consistent design work and branding. If choosing stock imagery, then from PixVault Basics please.
Should not have
• Not too much colour, or too consumer/youthful.

```html
<!DOCTYPE html>
<html lang="en">
<head>
<meta charset="utf-8">
<title>TWN – Cloud Services</title>
<link href="https://fonts.googleapis.com/css2?family=Montserrat:wght@400;500;600;700;800&display=swap" rel="stylesheet">
<style>
:root{
  --orange:#f7941d;
  --orange-dark:#e5801a;
  --navy:#0b1a2e;
  --navy-mid:#12305a;
  --blue:#1b66c9;
  --ink:#111418;
  --text:#4a4f57;
  --muted:#8a9099;
  --light:#f1f2f4;
  --white:#ffffff;
  --footer:#121417;
}
*{box-sizing:border-box;margin:0;padding:0}
html,body{width:1200px;height:5316px;overflow:hidden}
body{font-family:'Montserrat',Arial,sans-serif;color:var(--text);background:var(--white);position:relative}
section,header,footer{position:absolute;left:0;width:1200px}
.btn{display:inline-block;background:var(--orange);color:var(--white);font-weight:700;font-size:15px;letter-spacing:.5px;padding:13px 28px;border-radius:26px;text-transform:uppercase}
.accent{color:var(--orange)}
h2.section-title{font-size:44px;font-weight:800;color:var(--ink);text-align:center;line-height:1.12;text-transform:uppercase}

/* Header */
.site-header{top:0;height:112px;background:var(--white)}
.brand{position:absolute;left:96px;top:8px;font-size:72px;font-weight:800;color:var(--ink);letter-spacing:-2px;line-height:1}
.top-strip{position:absolute;right:96px;top:0;height:34px;background:var(--orange);display:flex;align-items:center;gap:22px;padding:0 18px;border-radius:0 0 6px 6px}
.top-strip a{color:var(--white);font-size:12px;font-weight:700;text-decoration:none}
.top-strip .social{width:18px;height:18px;border-radius:50%;border:2px solid var(--white);display:inline-block}
.main-nav{position:absolute;right:96px;top:54px;display:flex;align-items:center;gap:0}
.main-nav a{font-size:15px;font-weight:700;color:var(--ink);text-decoration:none;padding:10px 22px;border-right:1px solid #ccc}
.main-nav a.active{color:var(--orange);border-bottom:3px solid var(--orange)}
.nav-phone{display:flex;align-items:center;gap:8px;font-size:17px;font-weight:700;color:var(--ink);padding-left:20px}

/* Hero */
.hero{top:112px;height:668px}
.hero-media{position:absolute;inset:0;background:radial-gradient(ellipse at 72% 35%,#dfe9f5 0%,#7fa9d8 18%,#1d5fb0 45%,#0a2a5c 80%,#061834 100%)}
.hero h1{position:absolute;left:96px;top:180px;font-size:46px;font-weight:800;color:var(--white);line-height:1.1;text-transform:uppercase}
.hero .btn{position:absolute;left:96px;top:330px}
.hero .tagline{position:absolute;right:370px;top:538px;font-size:22px;font-weight:800;color:var(--white);text-transform:uppercase}
.hero-tabs{position:absolute;left:108px;top:592px;width:992px;height:64px;display:flex}
.hero-tabs div{flex:1;display:flex;align-items:center;justify-content:center;gap:12px;color:var(--white);font-size:17px;font-weight:700;text-transform:uppercase}
.tab-dark{background:#1c3f68}
.tab-orange{background:var(--orange)}
.tab-deep{background:#183a61}

/* Promise */
.promise{top:780px;height:732px}
.promise h2{position:absolute;top:60px;left:0;width:1200px}
.promise .intro{position:absolute;top:168px;left:100px;width:1000px;font-size:14px;line-height:1.75;text-align:center;color:var(--text)}
.steps{position:absolute;top:278px;left:110px;width:980px;display:flex;justify-content:space-between}
.step{display:flex;align-items:center;gap:10px;width:310px}
.step-num{font-size:120px;font-weight:400;color:var(--orange);line-height:1}
.step-circle{width:240px;height:240px;border-radius:50%;border:2px solid #d9dce1;display:flex;flex-direction:column;align-items:center;justify-content:center;text-align:center;padding:0 40px;font-size:13px;line-height:1.5;color:var(--text)}
.step-circle svg{margin-bottom:10px}
.step-circle u{color:var(--orange);text-decoration:underline}
.promise .cta{position:absolute;top:616px;left:0;width:1200px;display:flex;justify-content:center;align-items:center;gap:20px;font-size:17px;color:var(--ink);font-weight:500}
.promise .cta b{color:var(--orange)}
.btn-small{display:inline-flex;align-items:center;gap:8px;background:var(--orange);color:var(--white);font-size:13px;font-weight:700;padding:10px 22px;border-radius:22px;text-transform:uppercase}

/* Software */
.software{top:1512px;height:464px}
.software-media{position:absolute;inset:0;background:linear-gradient(180deg,#0b2340 0%,#123a66 45%,#0a1e36 100%)}
.software h2{position:absolute;top:128px;left:200px;width:800px;text-align:center;color:var(--white);font-size:34px;font-weight:800;line-height:1.2;text-transform:uppercase}
.software .btn-small{position:absolute;top:292px;left:514px}

/* Providers */
.providers{top:1976px;height:576px}
.providers h2{position:absolute;top:92px;left:0;width:1200px}
.provider-row{position:absolute;top:196px;left:100px;width:880px;display:flex;gap:20px;align-items:center}
.provider-row{left:60px;width:1080px}
.arrow{width:40px;display:flex;justify-content:center}
.provider-card{width:280px;height:320px;border-radius:18px;display:flex;flex-direction:column;align-items:center;justify-content:center;gap:40px}
.provider-card.orange{background:var(--orange)}
.provider-card.dark{background:#2b2d31;height:348px}
.provider-card.blue{background:var(--blue)}
.provider-name{display:flex;align-items:center;gap:10px;color:var(--white);font-size:30px;font-weight:700}
.provider-name i{width:22px;height:22px;border-radius:50%;background:var(--white);display:inline-block}
.provider-card .view{background:var(--white);color:var(--ink);font-size:13px;font-weight:700;padding:10px 28px;border-radius:20px;text-transform:uppercase}

/* Advice */
.advice{top:2552px;height:488px;background:var(--light)}
.advice .copy{position:absolute;left:96px;top:144px;width:480px}
.advice h3{font-size:22px;font-weight:800;color:var(--ink);line-height:1.25;text-transform:uppercase;margin-bottom:14px}
.advice p{font-size:14px;line-height:1.75}
.advice-media{position:absolute;right:0;top:0;width:600px;height:488px;background:linear-gradient(120deg,#1a4f8a 0%,#0c2a4e 55%,#203246 100%)}

/* Evaporate */
.evaporate{top:3040px;height:420px}
.evaporate h2{position:absolute;top:78px;left:0;width:1200px;font-size:38px}
.saving{position:absolute;left:200px;top:164px;width:236px;height:236px;border-radius:50%;background:var(--ink);display:flex;align-items:center;justify-content:center}
.saving div{width:170px;height:170px;border-radius:50%;background:var(--orange);color:var(--white);display:flex;flex-direction:column;align-items:center;justify-content:center;font-weight:800}
.saving .pct{font-size:48px;line-height:1}
.saving .lbl{font-size:17px}
.evaporate .copy{position:absolute;left:470px;top:172px;width:560px;font-size:14px;line-height:1.75}
.evaporate .copy p{margin-bottom:10px}

/* Started */
.started{top:3460px;height:400px}
.started-media{position:absolute;inset:0;background:linear-gradient(180deg,#071526 0%,#0e2f55 60%,#0a203b 100%)}
.started h2{position:absolute;top:108px;left:0;width:1200px;text-align:center;color:var(--white);font-size:34px;font-weight:800;text-transform:uppercase}
.started p{position:absolute;top:168px;left:250px;width:700px;text-align:center;color:#cfd7e2;font-size:14px;line-height:1.7}
.started .actions{position:absolute;top:250px;left:0;width:1200px;display:flex;justify-content:center;gap:14px}

/* Blog */
.blog{top:3860px;height:540px}
.blog h2{position:absolute;top:52px;left:0;width:1200px;font-size:38px}
.posts{position:absolute;top:128px;left:100px;width:1000px;display:flex;justify-content:space-between}
.post{width:310px}
.post-media{height:264px;border-radius:4px;position:relative}
.post:nth-child(1) .post-media{background:linear-gradient(135deg,#1a3354,#0e1a2c)}
.post:nth-child(2) .post-media{background:linear-gradient(135deg,#6e8cb0,#2b4a72)}
.post:nth-child(3) .post-media{background:linear-gradient(135deg,#2a7fd6,#0b3b7a)}
.post-media .dot{position:absolute;right:-8px;bottom:-14px;width:30px;height:30px;border-radius:50%;background:var(--orange)}
.post .date{font-size:12px;color:var(--muted);margin:14px 0 8px;display:flex;align-items:center;gap:6px}
.post h4{font-size:19px;font-weight:700;color:var(--ink);line-height:1.3}

/* Trusted */
.trusted{top:4400px;height:440px}
.trusted h2{position:absolute;top:52px;left:0;width:1200px;font-size:48px}
.clients{position:absolute;top:150px;left:110px;width:980px;display:grid;grid-template-columns:repeat(5,1fr);row-gap:70px}
.client{display:flex;align-items:center;justify-content:center;gap:8px;height:60px;font-size:15px;font-weight:700;color:#20314f;text-align:center}
.client i{width:16px;height:16px;background:#20314f;display:inline-block;flex:none}

/* Footer */
.site-footer{top:4840px;height:476px;background:var(--footer);color:#c8ccd2}
.footer-cols{position:absolute;top:62px;left:100px;width:1000px;display:flex;gap:56px}
.footer-col h5{color:var(--white);font-size:14px;font-weight:700;text-transform:uppercase;margin-bottom:14px}
.footer-col li{list-style:none;font-size:13px;line-height:1.85}
.footer-col .sub{margin-top:18px}
.badges{display:flex;gap:12px;margin-top:14px}
.badges span{width:56px;height:56px;border-radius:50%;background:#2f5ea8}
.badges span+span{background:#3a3d43;border-radius:6px}
.contact-line{display:flex;gap:10px;font-size:13px;line-height:1.6;margin-bottom:8px}
.contact-line svg{flex:none;margin-top:3px}
.footer-bar{position:absolute;bottom:0;left:0;width:1200px;height:56px;border-top:1px solid #2a2d32;display:flex;justify-content:space-between;align-items:center;padding:0 100px;font-size:12px}
.footer-bar nav{display:flex;gap:22px}
</style>
</head>
<body>

<header class="site-header">
  <div class="brand">TWN</div>
  <div class="top-strip">
    <a>PARTNERS</a><a>BLOG</a><a>ABOUT US</a><a>CONTACT US</a>
    <span class="social"></span><span class="social"></span><span class="social"></span>
  </div>
  <nav class="main-nav">
    <a class="active">HOME</a><a>CLOUD</a><a>SERVICES</a><a>SOFTWARE</a>
    <span class="nav-phone">
      <svg width="18" height="18" viewBox="0 0 24 24"><path fill="#f7941d" d="M6.6 10.8a15 15 0 0 0 6.6 6.6l2.2-2.2c.3-.3.7-.4 1-.2 1.1.4 2.3.6 3.6.6.6 0 1 .4 1 1V20c0 .6-.4 1-1 1A17 17 0 0 1 3 4c0-.6.4-1 1-1h3.5c.6 0 1 .4 1 1 0 1.3.2 2.5.6 3.6.1.3 0 .7-.2 1z"/></svg>
      01632 960705
    </span>
  </nav>
</header>

<section class="hero">
  <div class="hero-media" role="img" aria-label="Glowing digital cloud floating above a blue data network"></div>
  <h1>Operating under<br>a cloud?</h1>
  <span class="btn">Get started</span>
  <div class="tagline">There's a silver lining</div>
  <div class="hero-tabs">
    <div class="tab-dark">
      <svg width="22" height="22" viewBox="0 0 24 24" fill="none" stroke="#fff" stroke-width="2"><rect x="3" y="6" width="18" height="12" rx="2"/><circle cx="12" cy="12" r="3"/></svg>Reducing costs</div>
    <div class="tab-orange">
      <svg width="22" height="22" viewBox="0 0 24 24" fill="none" stroke="#fff" stroke-width="2"><path d="M7 18a5 5 0 0 1 0-10 6 6 0 0 1 11 2 4 4 0 0 1-1 8z"/></svg>Migration</div>
    <div class="tab-deep">
      <svg width="22" height="22" viewBox="0 0 24 24" fill="none" stroke="#fff" stroke-width="2"><circle cx="9" cy="8" r="3"/><path d="M3 20c0-4 3-6 6-6s6 2 6 6"/><circle cx="17" cy="9" r="2"/></svg>Work with us</div>
  </div>
</section>

<section class="promise">
  <h2 class="section-title">Did the promise of cloud computing<br><span class="accent">happen for you?</span></h2>
  <p class="intro">We didn't think so! You're not alone. There are many companies just like you who believed in the promise of cloud computing but are now shackled by it. But there is a silver lining, which is that TWN has built a business around helping companies improve their cloud efficiencies, reduce costs and simplify their operations as a result. It can be summarised in three promises TWN makes to every client or partner.</p>
  <div class="steps">
    <div class="step"><span class="step-num">1</span>
      <div class="step-circle">
        <svg width="44" height="36" viewBox="0 0 44 36" fill="none" stroke="#4a4f57" stroke-width="2"><path d="M12 30a9 9 0 0 1 0-18 12 12 0 0 1 22 4 7 7 0 0 1-2 14z"/><path d="M22 14v10M18 20l4 4 4-4"/></svg>
        <span>You can <u>reduce cloud costs</u>, without needing to move supplier</span></div></div>
    <div class="step"><span class="step-num">2</span>
      <div class="step-circle">
        <svg width="44" height="36" viewBox="0 0 44 36" fill="none" stroke="#4a4f57" stroke-width="2"><path d="M12 30a9 9 0 0 1 0-18 12 12 0 0 1 22 4 7 7 0 0 1-2 14z"/><path d="M15 22h14M25 18l4 4-4 4"/></svg>
        <span>You can <u>migrate</u> from one cloud to another more easily</span></div></div>
    <div class="step"><span class="step-num">3</span>
      <div class="step-circle">
        <svg width="44" height="36" viewBox="0 0 44 36" fill="none" stroke="#4a4f57" stroke-width="2"><path d="M12 30a9 9 0 0 1 0-18 12 12 0 0 1 22 4 7 7 0 0 1-2 14z"/><path d="M16 22l4 4 8-8"/></svg>
        <span>You can <u>simplify</u> your cloud management &amp; choose your favoured provider</span></div></div>
  </div>
  <div class="cta">If you already know or want to talk to us just call <b>01632 960 705</b> or
    <span class="btn-small"><svg width="14" height="12" viewBox="0 0 24 18" fill="none" stroke="#fff" stroke-width="2"><rect x="1" y="1" width="22" height="16"/><path d="M1 1l11 9 11-9"/></svg>Send an email</span></div>
</section>

<section class="software">
  <div class="software-media" role="img" aria-label="Rows of illuminated server racks in a data centre"></div>
  <h2>Your cloud, your tools a suite of software to simplify deployment</h2>
  <span class="btn-small">Cloud software</span>
</section>

<section class="providers">
  <h2 class="section-title">How hard is it to movey<br><span class="accent">our cloud?</span></h2>
  <div class="provider-row">
    <div class="arrow"><svg width="16" height="24" viewBox="0 0 16 24"><path d="M14 2L4 12l10 10" fill="none" stroke="#111418" stroke-width="4"/></svg></div>
    <div class="provider-card orange"><div class="provider-name"><i></i>StratoHost</div><span class="view">View more</span></div>
    <div class="provider-card dark"><div class="provider-name"><i></i>Nimbus Cloud</div><span class="view">View more</span></div>
    <div class="provider-card blue"><div class="provider-name"><i></i>Cirrus</div><span class="view">View more</span></div>
    <div class="arrow"><svg width="16" height="24" viewBox="0 0 16 24"><path d="M2 2l10 10L2 22" fill="none" stroke="#111418" stroke-width="4"/></svg></div>
  </div>
</section>

<section class="advice">
  <div class="copy">
    <h3>Knowledgeable independent<br>advice matters</h3>
    <p>Traditionally, the balance of power lies with your host, who has no interest in you moving to another platform. It may also be that your cloud supplier is a linked to your IT firm, developer or even staff preferences – and in some cases they will specialise in only one of these suppliers. It's time to break free. TWN equips companies, resellers and consultants with the power to choose, to negotiate, to move. We can do this for you.</p>
  </div>
  <div class="advice-media" role="img" aria-label="Two IT consultants reviewing a laptop in a server room"></div>
</section>

<section class="evaporate">
  <h2 class="section-title">Make your cloud <span class="accent">costs evaporate</span></h2>
  <div class="saving"><div><span class="pct">20%</span><span class="lbl">CHEAPER</span></div></div>
  <div class="copy">
    <p>As cloud costs continue to escalate, and as you suddenly hit new tiers of spend, you may feel helpless in the face of rising costs.</p>
    <p>However, even taking the cost of moving into account, TWN has estimated the average client will save 20% of spend on their cloud by using us to find the best solution and help you to move there.</p>
    <span class="btn-small">See case studies</span>
  </div>
</section>

<section class="started">
  <div class="started-media" role="img" aria-label="Dark blue abstract network of glowing data lines"></div>
  <h2>Let's get started</h2>
  <p>If you would like to speak to a friendly and helpful member of our team, ask questions, discuss option or to help with anything on your mind, please get in touch.</p>
  <div class="actions">
    <span class="btn-small">
      <svg width="13" height="13" viewBox="0 0 24 24"><path fill="#fff" d="M6.6 10.8a15 15 0 0 0 6.6 6.6l2.2-2.2c.3-.3.7-.4 1-.2 1.1.4 2.3.6 3.6.6.6 0 1 .4 1 1V20c0 .6-.4 1-1 1A17 17 0 0 1 3 4c0-.6.4-1 1-1h3.5c.6 0 1 .4 1 1 0 1.3.2 2.5.6 3.6.1.3 0 .7-.2 1z"/></svg>Call 01632 960 705</span>
    <span class="btn-small"><svg width="14" height="12" viewBox="0 0 24 18" fill="none" stroke="#fff" stroke-width="2"><rect x="1" y="1" width="22" height="16"/><path d="M1 1l11 9 11-9"/></svg>Send an email</span>
  </div>
</section>

<section class="blog">
  <h2 class="section-title">TWN <span class="accent">blog</span></h2>
  <div class="posts">
    <article class="post"><div class="post-media" role="img" aria-label="Engineer working at monitors in a dark office"><span class="dot"></span></div>
      <div class="date"><svg width="12" height="12" viewBox="0 0 24 24" fill="none" stroke="#8a9099" stroke-width="2"><rect x="3" y="5" width="18" height="16"/><path d="M3 10h18"/></svg>29 Oct 2022</div>
      <h4>Lorem ipsum it at, consectetur adipiscing elit, sed do</h4></article>
    <article class="post"><div class="post-media" role="img" aria-label="Technician checking a tablet between server racks"><span class="dot"></span></div>
      <div class="date"><svg width="12" height="12" viewBox="0 0 24 24" fill="none" stroke="#8a9099" stroke-width="2"><rect x="3" y="5" width="18" height="16"/><path d="M3 10h18"/></svg>29 Oct 2022</div>
      <h4>Lorem ipsum it at, consectetur adipiscing elit, sed do</h4></article>
    <article class="post"><div class="post-media" role="img" aria-label="Close-up of a blue glowing circuit board"><span class="dot"></span></div>
      <div class="date"><svg width="12" height="12" viewBox="0 0 24 24" fill="none" stroke="#8a9099" stroke-width="2"><rect x="3" y="5" width="18" height="16"/><path d="M3 10h18"/></svg>29 Oct 2022</div>
      <h4>Lorem ipsum it at, consectetur adipiscing elit, sed do</h4></article>
  </div>
</section>

<section class="trusted">
  <h2 class="section-title">Trusted <span class="accent">by</span></h2>
  <div class="clients">
    <div class="client"><i></i>Northwell Assurance</div>
    <div class="client"><i></i>Civic Bureau</div>
    <div class="client"><i></i>Irisline</div>
    <div class="client"><i></i>Dalefield</div>
    <div class="client"><i></i>Kairo Systems</div>
    <div class="client"><i></i>Meridian</div>
    <div class="client"><i></i>Bright Futures Trust</div>
    <div class="client"><i></i>Parcel Point</div>
    <div class="client"><i></i>ClearView Optics</div>
    <div class="client"><i></i>Northwell Assurance</div>
  </div>
</section>

<footer class="site-footer">
  <div class="footer-cols">
    <div class="footer-col"><h5>Cloud services</h5>
      <ul><li>StratoHost</li><li>Cirrus</li><li>Nimbus</li><li>Helix Data</li><li>Corelane</li><li>Bluewell</li><li>Others</li><li>Private Cloud</li></ul></div>
    <div class="footer-col"><h5>Services</h5>
      <ul><li>Cloud Cost Review</li><li>Migration Planning</li><li>Migration Execution</li><li>Security &amp; Compliance</li></ul>
      <h5 class="sub">Software</h5>
      <ul><li>SkyDeck</li><li>Portwise</li></ul></div>
    <div class="footer-col"><h5>About TWN</h5>
      <ul><li>Blog</li><li>Partners</li><li>About Us</li><li>Contact Us</li></ul>
      <div class="badges"><span></span><span></span></div></div>
    <div class="footer-col"><h5>Connect</h5>
      <div class="contact-line"><svg width="12" height="14" viewBox="0 0 24 28"><path fill="#f7941d" d="M12 0a10 10 0 0 0-10 10c0 8 10 18 10 18s10-10 10-18A10 10 0 0 0 12 0zm0 14a4 4 0 1 1 0-8 4 4 0 0 1 0 8z"/></svg><span>Harbour House, Mill Lane<br>Eastbridge EB4 7QT<br>United Kingdom</span></div>
      <div class="contact-line"><svg width="12" height="12" viewBox="0 0 24 24"><path fill="#f7941d" d="M6.6 10.8a15 15 0 0 0 6.6 6.6l2.2-2.2c.3-.3.7-.4 1-.2 1.1.4 2.3.6 3.6.6.6 0 1 .4 1 1V20c0 .6-.4 1-1 1A17 17 0 0 1 3 4c0-.6.4-1 1-1h3.5c.6 0 1 .4 1 1 0 1.3.2 2.5.6 3.6.1.3 0 .7-.2 1z"/></svg><span>01632 960705</span></div>
      <div class="contact-line"><svg width="12" height="10" viewBox="0 0 24 18" fill="none" stroke="#f7941d" stroke-width="2.5"><rect x="1" y="1" width="22" height="16"/><path d="M1 1l11 9 11-9"/></svg><span>hello@twncloud.co</span></div>
      <h5 class="sub">Follow on</h5>
      <div class="contact-line"><svg width="12" height="12" viewBox="0 0 12 12"><rect width="12" height="12" fill="#f7941d"/></svg><span>Linkspace</span></div>
    </div>
  </div>
  <div class="footer-bar">
    <span>©Copyright ©2022 TWN . All Rights Reserved.</span>
    <nav><span>Sitemap</span><span>Terms of Use</span><span>Privacy and Cookies Policy</span></nav>
  </div>
</footer>

</body>
</html>
```